Bluestone Freight

We are a 3PL freight brokerage company looking to create a website to attract new customers. Some ideas on how other freight websites look is located at these links, https://www.marigoldhaulerline.com/services, https://quillmarkcargo.com/freight-brokerage/.
We would like to have a quote feature implemented into this website.

We specialize in heavy-haul, specialized loads, flatbed, and dry vans.

```html
<!DOCTYPE html>
<html lang="en">
<head>
<meta charset="utf-8">
<title>Bluestone Freight — 3PL Freight Brokerage</title>
<link href="https://fonts.googleapis.com/css2?family=Poppins:ital,wght@0,400;0,500;0,600;1,600&family=Russo+One&display=swap" rel="stylesheet">
<style>
:root{
  --navy:#1b3664;
  --gold:#ad8a24;
  --gold-dark:#96771c;
  --ink:#222;
  --muted:#555;
  --dark:#1e1e1e;
  --light:#f3f3f3;
  --white:#fff;
}
*{box-sizing:border-box;margin:0;padding:0}
html,body{width:1200px;height:4448px;overflow:hidden}
body{position:relative;font-family:'Poppins',sans-serif;color:var(--ink);background:var(--white)}
.abs{position:absolute}
.display{font-family:'Russo One',sans-serif;color:var(--navy);letter-spacing:.5px}
.section-title{position:absolute;left:0;width:1200px;text-align:center;font-size:33px;line-height:45px}

/* header */
.brand{position:absolute;font-family:'Russo One',sans-serif;color:var(--navy);font-size:19px;line-height:22px;display:flex;align-items:center;gap:10px}
.brand-mark{width:18px;height:18px;background:var(--gold)}
.topbar{position:absolute;top:12px;right:72px;font-size:13px;display:flex;gap:48px;color:var(--ink)}
.topbar span{display:flex;align-items:center;gap:8px}
.nav{position:absolute;top:60px;left:465px;display:flex;gap:45px;font-size:14.5px}
.nav a{color:var(--ink);text-decoration:none;display:flex;align-items:center;gap:4px}
.nav a::after{content:"";width:5px;height:5px;border-radius:50%;background:var(--gold)}
.quote-btn{position:absolute;left:938px;top:48px;width:190px;height:47px;background:var(--gold);color:#fff;font-size:13.5px;font-weight:600;display:flex;align-items:center;justify-content:center;clip-path:polygon(14px 0,100% 0,100% 100%,0 100%)}

/* buttons */
.btn{position:absolute;height:45px;background:var(--navy);color:#fff;font-size:13px;font-weight:600;display:flex;align-items:center;padding-left:22px}
.btn-cap{position:absolute;right:0;top:0;width:44px;height:100%;background:var(--gold);clip-path:polygon(12px 0,100% 0,100% 100%,0 100%);display:flex;align-items:center;justify-content:flex-end;padding-right:8px}

/* hero */
.hero-photo{position:absolute;left:0;top:104px;width:1200px;height:576px;background:linear-gradient(180deg,#b7bcc0 0%,#9ea3a7 45%,#6c6f72 75%,#55585b 100%)}
.hero-head{position:absolute;left:681px}

/* cards */
.card{position:absolute;width:338px}
.card-photo{position:absolute;left:0;top:0;width:338px}
.card-panel{position:absolute;background:#fff;box-shadow:0 4px 14px rgba(0,0,0,.08)}
.card-title{position:absolute;left:24px;top:40px;font-size:17px;font-weight:500;color:var(--ink)}
.card-text{position:absolute;left:24px;top:80px;width:240px;font-size:12.5px;line-height:22px;color:var(--ink)}
.card-icon{position:absolute;width:76px;height:76px;border-radius:50%;background:#fff;border:3px solid var(--navy);display:flex;align-items:center;justify-content:center;box-shadow:0 0 0 5px rgba(255,255,255,.7)}

.pager{position:absolute;display:flex;gap:22px;font-size:13px;align-items:center}
.pager .on{width:26px;height:26px;border:1.5px solid var(--gold);border-radius:50%;color:var(--gold);display:flex;align-items:center;justify-content:center}

/* about */
.about-title{position:absolute;left:71px;top:1448px;color:#fff;font-size:33px}
.about-text{position:absolute;left:71px;top:1504px;width:500px;color:#fff;font-size:13px;line-height:32px}

/* features */
.feat{position:absolute;width:260px}
.feat h3{font-size:19px;font-weight:600;margin-bottom:8px}
.feat p{font-size:13px;line-height:25px;color:var(--ink)}
.feat.left{text-align:right}
.feat-icon{position:absolute;width:104px;height:104px;border-radius:50%;background:var(--gold);display:flex;align-items:center;justify-content:center}

/* testimonial */
.testi-box{position:absolute;left:425px;top:2539px;width:551px;height:181px;background:#fff}
.testi-quote{position:absolute;left:65px;top:36px;width:410px;font-size:13px;line-height:23px}
.testi-name{position:absolute;left:65px;top:115px;font-size:13px;font-weight:600;font-style:italic;color:var(--gold)}
.testi-role{position:absolute;left:65px;top:135px;font-size:11px;color:var(--muted)}

/* blog */
.meta{position:absolute;left:24px;top:48px;font-size:12.5px;display:flex;gap:55px}
.meta span{display:flex;align-items:center;gap:8px}

/* contact form */
.field{position:absolute;border:1.5px solid #cfcfcf;background:#fff;font-size:13px;color:var(--ink);padding:12px 14px}

/* footer */
.foot-head{position:absolute;top:4068px;color:var(--gold);font-size:16px;letter-spacing:.5px}
.foot-text{position:absolute;color:#fff;font-size:13px;line-height:22px}
.foot-links{position:absolute;left:739px;top:4126px;color:#fff;font-size:13.5px;list-style:none}
.foot-links li{height:31.5px;display:flex;align-items:center;gap:12px}
.foot-links li::before{content:"";width:6px;height:6px;border-top:1.5px solid #fff;border-right:1.5px solid #fff;transform:rotate(45deg)}
.copyright{position:absolute;left:0;top:4395px;width:1200px;height:53px;background:var(--gold);display:flex;align-items:center;justify-content:center;font-size:12.5px;color:var(--dark)}
</style>
</head>
<body>

<!-- Header -->
<div class="brand" style="left:71px;top:40px"><span class="brand-mark"></span>BLUESTONE<br>FREIGHT</div>
<div class="topbar">
  <span><svg width="13" height="13" viewBox="0 0 24 24"><path d="M6.6 10.8a15 15 0 0 0 6.6 6.6l2.2-2.2a1 1 0 0 1 1-.25 11.4 11.4 0 0 0 3.6.6 1 1 0 0 1 1 1V20a1 1 0 0 1-1 1A17 17 0 0 1 3 4a1 1 0 0 1 1-1h3.5a1 1 0 0 1 1 1c0 1.25.2 2.45.6 3.6a1 1 0 0 1-.25 1z" fill="#333"/></svg>602-555-0142 or Toll Free 800-555-0199</span>
  <span><svg width="14" height="11" viewBox="0 0 24 18"><rect x="1" y="1" width="22" height="16" fill="none" stroke="#333" stroke-width="2"/><path d="M1 1l11 9 11-9" fill="none" stroke="#333" stroke-width="2"/></svg>sales@bluestonefreight.com</span>
</div>
<nav class="nav"><a>Home</a><a>About</a><a>Services</a><a>Blog</a><a>Contact</a></nav>
<div class="quote-btn">Get A Quote Now</div>

<!-- Hero -->
<div class="hero-photo" role="img" aria-label="Photo of a red container truck parked in front of a grey warehouse"></div>
<svg class="abs" style="left:0;top:104px" width="1200" height="580" viewBox="0 0 1200 580">
  <polygon points="648,117 1070,117 1122,268 1070,418 565,418" fill="#fff"/>
  <polygon points="0,540 1200,495 1200,540 0,576" fill="var(--gold)"/>
  <polygon points="0,576 1200,540 1200,580 0,580" fill="#fff"/>
</svg>
<div class="hero-head display" style="top:272px;font-size:28px">WE ARE A</div>
<div class="hero-head display" style="top:306px;font-size:53px">3PL FREIGHT</div>
<div class="hero-head display" style="top:369px;font-size:29px">BROKERAGE COMPANY</div>
<div class="btn" style="left:681px;top:430px;width:170px;height:47px">Contact Now<span class="btn-cap"><svg width="22" height="22" viewBox="0 0 22 22"><circle cx="11" cy="11" r="10" fill="#fff"/><path d="M9 6.5l4.5 4.5L9 15.5" fill="none" stroke="var(--navy)" stroke-width="2.2"/></svg></span></div>

<!-- Services -->
<h2 class="section-title display" style="top:697px">SPECIAL LOGISTIC SERVICES</h2>

<div class="card" style="left:71px;top:765px;height:409px">
  <div class="card-photo" style="height:254px;background:linear-gradient(180deg,#7fa8d0 0%,#b9cbd9 45%,#6d7a6c 80%,#3b4540 100%)" role="img" aria-label="Photo of a car carrier truck loaded with vehicles"></div>
  <div class="card-panel" style="left:24px;top:211px;width:288px;height:198px">
    <div class="card-title">Heavy-Haul</div>
    <p class="card-text">It is a long established fact that a reader will be distracted by the readable content .</p>
    <div class="btn" style="right:0;bottom:0;width:150px">Read More<span class="btn-cap"><svg width="20" height="20" viewBox="0 0 22 22"><circle cx="11" cy="11" r="10" fill="#fff"/><path d="M9 6.5l4.5 4.5L9 15.5" fill="none" stroke="var(--navy)" stroke-width="2.2"/></svg></span></div>
  </div>
  <div class="card-icon" style="left:212px;top:143px"><svg width="38" height="38" viewBox="0 0 40 40" fill="none" stroke="var(--navy)" stroke-width="2"><rect x="10" y="6" width="20" height="22" rx="3"/><rect x="13" y="10" width="14" height="8"/><circle cx="15" cy="23" r="1.5"/><circle cx="25" cy="23" r="1.5"/><path d="M13 28v4M27 28v4M6 14h4M30 14h4"/></svg></div>
</div>

<div class="card" style="left:432px;top:765px;height:409px">
  <div class="card-photo" style="height:254px;background:linear-gradient(180deg,#9aa3b5 0%,#c8b8a8 40%,#3a4f7a 75%,#4a4a4a 100%)" role="img" aria-label="Photo of a blue semi truck hauling a specialized load"></div>
  <div class="card-panel" style="left:24px;top:211px;width:288px;height:198px">
    <div class="card-title">Specialized Loads</div>
    <p class="card-text">It is a long established fact that a reader will be distracted by the readable content .</p>
    <div class="btn" style="right:0;bottom:0;width:150px">Read More<span class="btn-cap"><svg width="20" height="20" viewBox="0 0 22 22"><circle cx="11" cy="11" r="10" fill="#fff"/><path d="M9 6.5l4.5 4.5L9 15.5" fill="none" stroke="var(--navy)" stroke-width="2.2"/></svg></span></div>
  </div>
  <div class="card-icon" style="left:212px;top:143px"><svg width="38" height="38" viewBox="0 0 40 40" fill="none" stroke="var(--navy)" stroke-width="2"><path d="M20 5l13 7v16l-13 7-13-7V12z"/><path d="M7 12l13 7 13-7M20 19v16M13 8.5l13 7"/></svg></div>
</div>

<div class="card" style="left:791px;top:765px;height:409px">
  <div class="card-photo" style="height:254px;background:linear-gradient(180deg,#8fb0d6 0%,#c9d3da 40%,#d9dbdb 65%,#5b6a4f 100%)" role="img" aria-label="Photo of a white cargo van on a road"></div>
  <div class="card-panel" style="left:24px;top:211px;width:288px;height:198px">
    <div class="card-title">Dry Vans</div>
    <p class="card-text">It is a long established fact that a reader will be distracted by the readable content .</p>
    <div class="btn" style="right:0;bottom:0;width:150px">Read More<span class="btn-cap"><svg width="20" height="20" viewBox="0 0 22 22"><circle cx="11" cy="11" r="10" fill="#fff"/><path d="M9 6.5l4.5 4.5L9 15.5" fill="none" stroke="var(--navy)" stroke-width="2.2"/></svg></span></div>
  </div>
  <div class="card-icon" style="left:212px;top:143px"><svg width="40" height="38" viewBox="0 0 42 40" fill="none" stroke="var(--navy)" stroke-width="2"><path d="M12 12h17v16H12zM29 17h6l4 5v6H29"/><circle cx="17" cy="29" r="3" fill="#fff"/><circle cx="33" cy="29" r="3" fill="#fff"/><path d="M3 16h6M5 21h6M3 26h6"/></svg></div>
</div>

<div class="pager" style="left:574px;top:1201px"><span class="on">1</span><span>2</span></div>

<!-- About -->
<svg class="abs" style="left:0;top:1228px" width="1200" height="640" viewBox="0 1228 1200 640">
  <polygon points="475,1299 1200,1230 1200,1748 458,1810 717,1537" fill="url(#portGrad)" role="img" aria-label="Photo of a container port with cranes and stacked containers"/>
  <polygon points="0,1257 475,1299 717,1537 458,1810 0,1865" fill="var(--gold)"/>
  <defs>
    <linearGradient id="portGrad" x1="0" y1="0" x2="0" y2="1">
      <stop offset="0" stop-color="#c9d2dc"/><stop offset=".45" stop-color="#8fa3b8"/><stop offset=".7" stop-color="#6d5a5a"/><stop offset="1" stop-color="#2f3550"/>
    </linearGradient>
  </defs>
</svg>
<h2 class="about-title display">ABOUT US</h2>
<p class="about-text">Lorem Ipsum is simply dummy text of the printing and typesetting industry. Lorem Ipsum has been the industry's standard dummy text ever since the 1500s, when an unknown printer took a galley of type and scrambled it to make a type specimen book.</p>
<div class="btn" style="left:71px;top:1654px;width:170px;height:49px">Read More<span class="btn-cap"><svg width="22" height="22" viewBox="0 0 22 22"><circle cx="11" cy="11" r="10" fill="#fff"/><path d="M9 6.5l4.5 4.5L9 15.5" fill="none" stroke="var(--navy)" stroke-width="2.2"/></svg></span></div>

<!-- Features -->
<h2 class="section-title display" style="top:1891px">TOGETHER,WE HAVE YOUR LOGISTICAL<br>CHALLENGES COVERED.</h2>
<div class="abs" style="left:411px;top:2005px;width:380px;height:380px;border-radius:50%;background:linear-gradient(180deg,#6f8aa8 0%,#9aa4ad 45%,#5a5a5a 75%,#2c2c2c 100%)" role="img" aria-label="Round photo of a truck on a highway with a chevron overlay"></div>

<div class="feat left" style="left:97px;top:2026px"><h3>Scalability</h3><p>Lorem Ipsum is simply dummy text of the printing and typesetting industry.</p></div>
<div class="feat left" style="left:97px;top:2220px"><h3>Power Only</h3><p>Lorem Ipsum is simply dummy text of the printing and typesetting industry.</p></div>
<div class="feat" style="left:841px;top:2026px"><h3>Flatbed</h3><p>Lorem Ipsum is simply dummy text of the printing and typesetting industry.</p></div>
<div class="feat" style="left:841px;top:2220px"><h3>Full Truck Load</h3><p>Lorem Ipsum is simply dummy text of the printing and typesetting industry.</p></div>

<div class="feat-icon" style="left:369px;top:2032px"><svg width="56" height="56" viewBox="0 0 56 56" fill="none" stroke="#fff" stroke-width="2"><path d="M28 20l8 4v8l-8 4-8-4v-8z"/><path d="M28 4v12M28 40v12M4 28h12M40 28h12M11 11l8 8M45 11l-8 8M11 45l8-8M45 45l-8-8"/></svg></div>
<div class="feat-icon" style="left:369px;top:2224px"><svg width="56" height="56" viewBox="0 0 56 56" fill="none" stroke="#fff" stroke-width="2"><circle cx="28" cy="30" r="18"/><path d="M16 40l9-9 6 5 11-14M36 22h6v6"/></svg></div>
<div class="feat-icon" style="left:729px;top:2032px"><svg width="56" height="56" viewBox="0 0 56 56" fill="none" stroke="#fff" stroke-width="2"><rect x="8" y="14" width="22" height="30"/><path d="M30 24h10l8 10v10H30"/><circle cx="16" cy="45" r="3"/><circle cx="40" cy="45" r="3"/><path d="M12 22h14M12 30h14"/></svg></div>
<div class="feat-icon" style="left:729px;top:2224px"><svg width="56" height="56" viewBox="0 0 56 56" fill="none" stroke="#fff" stroke-width="2"><path d="M12 8v38h34"/><rect x="18" y="18" width="14" height="22"/><path d="M38 20v20M34 24h8"/><circle cx="16" cy="48" r="3"/><circle cx="44" cy="48" r="3"/></svg></div>

<!-- Testimonial -->
<div class="abs" style="left:0;top:2700px;width:1200px;height:780px;background:var(--light)"></div>
<svg class="abs" style="left:0;top:2345px" width="1200" height="520" viewBox="0 2345 1200 520" role="img" aria-label="Dark photo of a harbour with cranes at dusk">
  <polygon points="0,2387 1200,2349 1200,2790 0,2858" fill="#252525"/>
</svg>
<div class="abs" style="left:225px;top:2539px;width:200px;height:181px;background:linear-gradient(180deg,#3a3a3a,#1c1c1c)" role="img" aria-label="Portrait photo of the client"></div>
<div class="testi-box">
  <div class="abs" style="left:24px;top:30px;font-family:'Russo One',sans-serif;font-size:34px;line-height:30px;color:var(--navy)">”</div>
  <p class="testi-quote">Many desktop publishing packages and web page editors now use Lorem Ipsum as their default model text, and a search for 'lorem ipsum' .</p>
  <div class="testi-name">Mara Quinlan</div>
  <div class="testi-role">Head Of Society Chairs</div>
  <div class="abs" style="left:507px;top:49px;display:flex;flex-direction:column;align-items:center;gap:8px;font-size:12px">
    <span style="width:24px;height:24px;border:1.5px solid var(--gold);border-radius:50%;color:var(--gold);display:flex;align-items:center;justify-content:center">1</span>
    <span>2</span><span style="margin-top:8px">3</span>
  </div>
</div>

<!-- Blog -->
<h2 class="section-title display" style="top:2893px">GET THE LATEST NEWS,<br>ADVICE &amp; BEST PRACTICE FROM BLOG</h2>

<div class="card" style="left:71px;top:3008px;height:325px">
  <div class="card-photo" style="height:230px;background:linear-gradient(180deg,#5d6a75 0%,#98a3ab 50%,#6e6e6e 100%)" role="img" aria-label="Photo of a warehouse loading dock"></div>
  <div class="card-panel" style="left:24px;top:139px;width:285px;height:166px">
    <div class="meta"><span><svg width="12" height="12" viewBox="0 0 12 12"><rect x=".5" y="1.5" width="11" height="10" fill="none" stroke="#333"/><path d="M.5 4.5h11" stroke="#333"/></svg>April 12,2022</span><span><svg width="12" height="12" viewBox="0 0 12 12"><circle cx="6" cy="3.5" r="3" fill="#333"/><path d="M0 12a6 5 0 0 1 12 0z" fill="#333"/></svg>Admin</span></div>
    <p class="card-text" style="top:78px">It is a long established fact that a reader will be distracted</p>
    <div class="btn" style="left:62px;top:139px;width:166px">Read More<span class="btn-cap"><svg width="20" height="20" viewBox="0 0 22 22"><circle cx="11" cy="11" r="10" fill="#fff"/><path d="M9 6.5l4.5 4.5L9 15.5" fill="none" stroke="var(--navy)" stroke-width="2.2"/></svg></span></div>
  </div>
</div>

<div class="card" style="left:432px;top:3008px;height:325px">
  <div class="card-photo" style="height:230px;background:linear-gradient(180deg,#6b6b6b 0%,#a8a8a0 45%,#8a8a5a 75%,#5a5a5a 100%)" role="img" aria-label="Photo of a forklift moving pallets inside a warehouse"></div>
  <div class="card-panel" style="left:24px;top:139px;width:285px;height:166px">
    <div class="meta"><span><svg width="12" height="12" viewBox="0 0 12 12"><rect x=".5" y="1.5" width="11" height="10" fill="none" stroke="#333"/><path d="M.5 4.5h11" stroke="#333"/></svg>April 12,2022</span><span><svg width="12" height="12" viewBox="0 0 12 12"><circle cx="6" cy="3.5" r="3" fill="#333"/><path d="M0 12a6 5 0 0 1 12 0z" fill="#333"/></svg>Admin</span></div>
    <p class="card-text" style="top:78px">It is a long established fact that a reader will be distracted</p>
    <div class="btn" style="left:62px;top:139px;width:166px">Read More<span class="btn-cap"><svg width="20" height="20" viewBox="0 0 22 22"><circle cx="11" cy="11" r="10" fill="#fff"/><path d="M9 6.5l4.5 4.5L9 15.5" fill="none" stroke="var(--navy)" stroke-width="2.2"/></svg></span></div>
  </div>
</div>

<div class="card" style="left:791px;top:3008px;height:325px">
  <div class="card-photo" style="height:230px;background:linear-gradient(180deg,#8aa0b8 0%,#6d7f95 45%,#b08a5a 75%,#4d5560 100%)" role="img" aria-label="Photo of a large warehouse with high racking"></div>
  <div class="card-panel" style="left:24px;top:139px;width:285px;height:166px">
    <div class="meta"><span><svg width="12" height="12" viewBox="0 0 12 12"><rect x=".5" y="1.5" width="11" height="10" fill="none" stroke="#333"/><path d="M.5 4.5h11" stroke="#333"/></svg>April 12,2022</span><span><svg width="12" height="12" viewBox="0 0 12 12"><circle cx="6" cy="3.5" r="3" fill="#333"/><path d="M0 12a6 5 0 0 1 12 0z" fill="#333"/></svg>Admin</span></div>
    <p class="card-text" style="top:78px">It is a long established fact that a reader will be distracted</p>
    <div class="btn" style="left:62px;top:139px;width:166px">Read More<span class="btn-cap"><svg width="20" height="20" viewBox="0 0 22 22"><circle cx="11" cy="11" r="10" fill="#fff"/><path d="M9 6.5l4.5 4.5L9 15.5" fill="none" stroke="var(--navy)" stroke-width="2.2"/></svg></span></div>
  </div>
</div>

<div class="pager" style="left:546px;top:3363px"><span class="on">1</span><span>2</span><span>3</span></div>

<!-- Contact -->
<svg class="abs" style="left:124px;top:3532px" width="330" height="364" viewBox="0 0 330 364" role="img" aria-label="Photo of a truck on the road framed in a chevron shape">
  <defs><linearGradient id="chevGrad" x1="0" y1="0" x2="0" y2="1"><stop offset="0" stop-color="#d5d0c6"/><stop offset=".5" stop-color="#6c7888"/><stop offset="1" stop-color="#5a5046"/></linearGradient></defs>
  <polygon points="0,0 120,0 328,182 120,364 0,364 150,182" fill="url(#chevGrad)"/>
</svg>
<h2 class="abs display" style="left:521px;top:3522px;font-size:33px;line-height:45px">LOOKING FOR THE<br>BEST TRANSPORT SERVICES</h2>
<div class="field" style="left:521px;top:3640px;width:273px;height:46px">Name</div>
<div class="field" style="left:521px;top:3696px;width:273px;height:46px">Phone Number</div>
<div class="field" style="left:521px;top:3751px;width:273px;height:46px">Email</div>
<div class="field" style="left:800px;top:3640px;width:328px;height:157px">Message</div>
<div class="btn" style="left:521px;top:3810px;width:170px;height:48px">Send Now<span class="btn-cap"><svg width="22" height="22" viewBox="0 0 22 22"><circle cx="11" cy="11" r="10" fill="#fff"/><path d="M9 6.5l4.5 4.5L9 15.5" fill="none" stroke="var(--navy)" stroke-width="2.2"/></svg></span></div>

<!-- Footer -->
<svg class="abs" style="left:0;top:3900px" width="1200" height="495" viewBox="0 3900 1200 495" role="img" aria-label="Dark photo of a truck fleet behind the footer">
  <polygon points="0,3960 1200,3908 1200,4395 0,4395" fill="var(--gold)"/>
  <polygon points="0,3985 1200,3935 1200,4395 0,4395" fill="#1c1c1c"/>
</svg>

<div class="foot-head" style="left:71px">LOCATION</div>
<svg class="abs" style="left:71px;top:4133px" width="14" height="18" viewBox="0 0 14 18"><path d="M7 0a7 7 0 0 1 7 7c0 5-7 11-7 11S0 12 0 7a7 7 0 0 1 7-7z" fill="var(--gold)"/><circle cx="7" cy="7" r="2.5" fill="#1c1c1c"/></svg>
<p class="foot-text" style="left:101px;top:4126px;width:220px">Corporate Office<br>418 W Harbor Rd, Ste 2 Mesa, AZ</p>
<svg class="abs" style="left:71px;top:4214px" width="15" height="15" viewBox="0 0 24 24"><path d="M6.6 10.8a15 15 0 0 0 6.6 6.6l2.2-2.2a1 1 0 0 1 1-.25 11.4 11.4 0 0 0 3.6.6 1 1 0 0 1 1 1V20a1 1 0 0 1-1 1A17 17 0 0 1 3 4a1 1 0 0 1 1-1h3.5a1 1 0 0 1 1 1c0 1.25.2 2.45.6 3.6a1 1 0 0 1-.25 1z" fill="var(--gold)"/></svg>
<p class="foot-text" style="left:101px;top:4210px">123-555-0178</p>
<svg class="abs" style="left:71px;top:4256px" width="15" height="11" viewBox="0 0 24 18"><rect width="24" height="18" fill="var(--gold)"/><path d="M1 1l11 9 11-9" fill="none" stroke="#1c1c1c" stroke-width="2"/></svg>
<p class="foot-text" style="left:101px;top:4250px">bluestonefreight@mail.com</p>

<div class="foot-head" style="left:378px">NEWSLETTER</div>
<p class="foot-text" style="left:378px;top:4126px;width:290px;line-height:25px">Subscribe Our Newsletter To Get Our latest updates &amp; news</p>
<div class="abs" style="left:378px;top:4193px;width:295px;height:41px;background:#fff;display:flex;align-items:center;padding-left:16px;font-size:13px">Enter Your Mail Id</div>
<div class="abs" style="left:615px;top:4193px;width:58px;height:41px;background:var(--gold);clip-path:polygon(10px 0,100% 0,100% 100%,0 100%);display:flex;align-items:center;justify-content:center"><svg width="20" height="18" viewBox="0 0 20 18"><path d="M0 8L20 0 16 18 9 12 17 3 7 11z" fill="#fff"/></svg></div>
<div class="abs" style="left:378px;top:4262px;display:flex;gap:22px">
  <span style="width:16px;height:16px;border:2px solid #fff;border-radius:50%"></span>
  <span style="width:16px;height:16px;border:2px solid #fff;border-radius:50%"></span>
  <span style="width:16px;height:16px;border:2px solid #fff;border-radius:50%"></span>
  <span style="width:16px;height:16px;border:2px solid #fff;border-radius:50%"></span>
</div>

<div class="foot-head" style="left:739px">QUICK LINKS</div>
<ul class="foot-links"><li>Home</li><li>About</li><li>Services</li><li>Blog</li><li>Contact</li></ul>

<div class="brand" style="left:906px;top:4140px;color:#fff;font-size:24px;line-height:28px">BLUESTONE<br>FREIGHT</div>
<p class="foot-text" style="left:880px;top:4216px;width:270px;text-align:center;line-height:24.5px">Mon to Friday: 10.00 am - 7.00 pm<br>Sat : 10.00 am - 5.00pm<br>Sun : 10.00am - 2.00pm</p>

<div class="copyright">© 2022 bluestonefreight, All right Reserved</div>

</body>
</html>
```